Supplement Bottle Packaging and Design

We want to rebrand our current health supplements (see below). We do want it to be modern, vibrant and appealing supplement bottles. Very upscale and elegant as it targets primarily women.
NOTE: READ THE ATTACHED WORD DOCUMENT!
Bottle size: We are totally open to the bottle size and shape, as long it's a typical supplement bottle size to handle 90-120 capsules; what we mostly need is new bottle design/packaging. YOU DON’T HAVE TO USE THE CURRENT WHITE BOTTLE SHAPE, BUT ANYTHING MORE MODERN WOULD WORK!
Updates
We need more modern, clean sleek designs to choose from
Look and feel
Each slider illustrates characteristics of the customer's brand and the style your logo design should communicate.

```html
<!DOCTYPE html>
<html lang="en">
<head>
<meta charset="UTF-8">
<title>Luma Balance Formula – Label</title>
<link rel="stylesheet" href="https://fonts.googleapis.com/css2?family=Outfit:wght@300;400;500&display=swap">
<style>
  :root {
    --label-bg: #ececec;
    --ink: #2a2a2a;
    --ink-soft: #3d3d3d;
    --accent: #3f9a1c;
  }
  * { margin: 0; padding: 0; box-sizing: border-box; }
  html, body {
    width: 1200px;
    height: 1200px;
    overflow: hidden;
    background: var(--label-bg);
  }
  .label {
    position: relative;
    width: 1200px;
    height: 1200px;
    font-family: "Outfit", sans-serif;
    color: var(--ink);
    text-align: center;
  }
  .product-name {
    position: absolute;
    top: 330px;
    left: 0;
    right: 0;
    font-weight: 400;
    font-size: 86px;
    letter-spacing: 0.5px;
    line-height: 1;
  }
  .product-type {
    position: absolute;
    top: 440px;
    left: 0;
    right: 0;
    font-weight: 400;
    font-size: 26px;
    letter-spacing: 16px;
    padding-left: 16px;
    color: var(--ink-soft);
  }
  .accent-dot {
    position: absolute;
    top: 616px;
    left: 572px;
    width: 56px;
    height: 56px;
  }
  .benefit {
    position: absolute;
    top: 890px;
    left: 0;
    right: 0;
    font-weight: 300;
    font-size: 38px;
    color: var(--ink-soft);
  }
  .category {
    position: absolute;
    top: 948px;
    left: 0;
    right: 0;
    font-weight: 400;
    font-size: 32px;
    letter-spacing: 9px;
    padding-left: 9px;
  }
  .category .light { font-weight: 300; }
  .count {
    position: absolute;
    top: 1000px;
    left: 0;
    right: 0;
    font-weight: 400;
    font-size: 18px;
    letter-spacing: 0.5px;
  }
</style>
</head>
<body>
  <main class="label">
    <h1 class="product-name">Luma Balance</h1>
    <p class="product-type">FORMULA</p>
    <svg class="accent-dot" viewBox="0 0 56 56" aria-hidden="true">
      <circle cx="28" cy="28" r="26" fill="var(--accent)"/>
    </svg>
    <p class="benefit">Supports Healthy Hormone Levels</p>
    <p class="category"><span class="light">DIETARY</span> SUPPLEMENT</p>
    <p class="count">60 VEGETABLE CAPSULES</p>
  </main>
</body>
</html>
```